Saffron Lantern Court Business Card

I am looking for a business card desgined for my restaurant. It is an Indian restaurant, we are looking for something thats modern, yet traditional with the indian culture, we are looking for colors that match our logo. The logo is a design of the building with the name of the restaurant. for more information on the restaurant go to www.saffronlanterncourt.example

Industry/Entity Type

Indian Restaurant

Contact Information for Business Card

we are looking for somthing thats modern, yet traditional with the indian culture, we are looking for colors that match our logo. The logo is a design of the building with the name of the restaurant. for more information on the restaurant go to www.saffronlanterncourt.example

Requirements
Must have
• The logo that is attached,
• Name: Harvinder Oberoi,
• address of the restaurant: 7328 West Larkspur Rd, Phoenix, Arizona, 85213
• Phone: (602) 555-0147
• Fax: (602) 555-0193
• Restaurant Catering Banquet
• Website: www.SaffronLanternCourt.example
Nice to have
• wanted to get something that goes with the theme of the restaurant, which is traditional but also keep a very professional and modern touch

```html
<!DOCTYPE html>
<html lang="en">
<head>
<meta charset="utf-8">
<title>Saffron Lantern Court – Business Card</title>
<link rel="stylesheet" href="https://fonts.googleapis.com/css2?family=Federo&display=swap">
<style>
  :root {
    --page: #ffffff;
    --maroon-deep: #3a0f0c;
    --maroon: #5a1a12;
    --saffron-light: #f3c48a;
    --saffron: #e39550;
    --saffron-dark: #c8662a;
    --spice-red: #b8371d;
    --turmeric: #e0a23c;
    --ink: #8a1f1a;
    --curry: #d46b2c;
  }
  html, body {
    margin: 0;
    width: 1200px;
    height: 1200px;
    overflow: hidden;
    background: var(--page);
  }
  .sheet {
    position: relative;
    width: 1200px;
    height: 1200px;
  }
  .card {
    position: absolute;
    left: 102px;
    width: 996px;
    height: 548px;
    overflow: hidden;
    font-family: "Federo", sans-serif;
    color: var(--ink);
  }
  .card--front { top: 34px; }
  .card--back { top: 622px; }
  .card__art {
    position: absolute;
    inset: 0;
    width: 996px;
    height: 548px;
  }
  .card__text {
    position: absolute;
    left: 0;
    width: 100%;
    margin: 0;
    text-align: center;
    white-space: nowrap;
  }
  .brand-name {
    position: absolute;
    left: 245px;
    width: 500px;
    top: 98px;
    margin: 0;
    text-align: center;
    font-size: 66px;
    line-height: 76px;
    font-weight: 400;
    letter-spacing: 2px;
    text-transform: uppercase;
    color: var(--ink);
  }
  .front-web { top: 434px; left: -50px; font-size: 29px; }
  .back-web { top: 58px; left: -60px; font-size: 34px; }
  .back-name { top: 124px; left: -45px; font-size: 31px; }
  .back-phone { top: 190px; left: -45px; font-size: 31px; }
  .back-fax { top: 252px; left: -45px; font-size: 31px; }
  .back-address { top: 323px; left: -30px; font-size: 30px; }
</style>
</head>
<body>
<main class="sheet">

  <section class="card card--front">
    <svg class="card__art" viewBox="0 0 996 548" aria-hidden="false">
      <defs>
        <radialGradient id="frontGlow" cx="0.45" cy="0.45" r="0.7">
          <stop offset="0" stop-color="var(--saffron-light)"/>
          <stop offset="0.6" stop-color="var(--saffron)"/>
          <stop offset="1" stop-color="var(--saffron-dark)"/>
        </radialGradient>
        <radialGradient id="spiceTone" cx="0.6" cy="0.4" r="0.6">
          <stop offset="0" stop-color="var(--spice-red)" stop-opacity="0.75"/>
          <stop offset="0.5" stop-color="var(--turmeric)" stop-opacity="0.55"/>
          <stop offset="1" stop-color="var(--saffron)" stop-opacity="0"/>
        </radialGradient>
        <clipPath id="frontOval">
          <ellipse cx="470" cy="190" rx="620" ry="345"/>
        </clipPath>
      </defs>
      <rect class="paisley-field" width="996" height="548" fill="var(--maroon-deep)" role="img" aria-label="Dark maroon paisley pattern background"/>
      <ellipse cx="470" cy="190" rx="620" ry="345" fill="url(#frontGlow)"/>
      <g clip-path="url(#frontOval)">
        <rect class="spice-photo" x="560" y="0" width="436" height="480" fill="url(#spiceTone)" role="img" aria-label="Photograph of bowls of ground spices"/>
      </g>
    </svg>
    <h1 class="brand-name">Saffron<br>Lantern<br>Court</h1>
    <p class="card__text front-web">www.SaffronLanternCourt.example</p>
  </section>

  <section class="card card--back">
    <svg class="card__art" viewBox="0 0 996 548">
      <defs>
        <radialGradient id="backGlow" cx="0.5" cy="0.45" r="0.75">
          <stop offset="0" stop-color="var(--saffron-light)"/>
          <stop offset="0.6" stop-color="var(--saffron)"/>
          <stop offset="1" stop-color="var(--saffron-dark)"/>
        </radialGradient>
        <radialGradient id="foodTone" cx="0.4" cy="0.45" r="0.6">
          <stop offset="0" stop-color="var(--curry)" stop-opacity="0.8"/>
          <stop offset="0.6" stop-color="var(--saffron-dark)" stop-opacity="0.4"/>
          <stop offset="1" stop-color="var(--saffron)" stop-opacity="0"/>
        </radialGradient>
      </defs>
      <rect class="paisley-field" width="996" height="548" fill="var(--maroon-deep)" role="img" aria-label="Dark maroon paisley pattern background"/>
      <path d="M0 0 H996 V548 H640 Q230 500 0 305 Z" fill="url(#backGlow)"/>
      <rect class="food-photo" x="0" y="0" width="470" height="320" fill="url(#foodTone)" role="img" aria-label="Faded photograph of curry and flatbread dishes"/>
    </svg>
    <p class="card__text back-web">www.SaffronLanternCourt.example</p>
    <p class="card__text back-name">Harvinder Oberoi</p>
    <p class="card__text back-phone">T:&nbsp; (602) 555-0147</p>
    <p class="card__text back-fax">F:&nbsp; (602) 555-0193</p>
    <p class="card__text back-address">7328 West Larkspur Rd, Phoenix, Arizona, 85213</p>
  </section>

</main>
</body>
</html>
```